Craft Beacon K.V. (Toronto) - Training Our Millenials

This website is going to be a trades and learning platform where you can sign-up and register for different trades that may suit your interests. With this site I want people to be able to pull up an on-line application form with a submit button to register on-line. I would also like to see this website include interactive images with links or landing pages to the trade or service they will be registering for. I would like it to be friendly and straightforward to anyone trying to apply. Since this program will originate in Toronto, Ontario Canada, I would also like that to be reflected in the web design(RB Spire, Red Maple Leaf etc.) The following trades learning platforms will be included in my services and would like that to be reflected by 2-3 roll-over images for each trade profession:
-ELECTRICAL
-MECHANICAL
-PLUMBING
-CONTRACTORS
-FLOORING
-DRY-WALL
-ROOFING
-HANDY-MAN
-CARPENTRY
-MAINTENANCE
**REFER TO THIS WEBSITE FOR TEMPLATE OF IDEA
http://www.lunvaskills.com/fernpaths/learning.html
Target Market(s)
Employers, Youth, Adults, Un-Employed, Agencies
Industry/Entity Type
Trade
Coding
Coded - Design and coding required
Number of Pages Required
1 page
Requirements
Must have
- Must have images supporting each profession/trade, must include register on-line function, must include user friendly icons and themes, must represent Toronto, Canada in the web design. Must be a modern design with a professional feel.
Nice to have
- on-line support function where the admin user can communicate with individuals interested in asking questions or concerns.
Should not have
- should not be dull

```html
<!DOCTYPE html>
<html lang="en">
<head>
<meta charset="utf-8">
<title>Craft Beacon K.V. – Training Our Millennials</title>
<link href="https://fonts.googleapis.com/css2?family=Roboto:wght@400;500;700&family=Oswald:wght@400;500&display=swap" rel="stylesheet">
<style>
:root{
  --teal:#0aa68a;
  --lime:#8cc63f;
  --lime-light:#a6d45a;
  --sky:#3a8fd6;
  --footer:#0b8bcf;
  --orange:#f0642a;
  --red:#e0322a;
  --dark:#1d1d1d;
  --text:#333;
  --muted:#777;
  --white:#fff;
}
*{box-sizing:border-box;margin:0;padding:0}
html,body{width:1200px;height:2493px;overflow:hidden;background:var(--white)}
body{position:relative;font-family:'Roboto',Arial,sans-serif;color:var(--text)}
.abs{position:absolute}
a{color:inherit;text-decoration:none}

/* header */
.site-header{position:absolute;left:0;top:0;width:1200px;height:125px;background:var(--white)}
.brand{position:absolute;left:98px;top:24px;display:flex;align-items:center;gap:10px}
.brand-mark{width:76px;height:76px;border-radius:50%;border:4px solid var(--orange)}
.brand-name{font-size:17px;font-weight:700;color:var(--orange)}
.account{position:absolute;right:100px;top:20px;display:flex;gap:14px;align-items:center;font-size:12px}
.btn-signup{background:var(--lime);color:var(--white);padding:5px 12px;border-radius:2px;font-weight:500}
.main-nav{position:absolute;right:100px;top:62px;display:flex;align-items:center;gap:0}
.main-nav a{font-size:12.5px;font-weight:500;color:#444;padding:12px 15px;text-transform:uppercase;white-space:nowrap}
.main-nav .is-active{color:var(--red);border:2px solid var(--red);border-radius:50%;padding:14px 12px}

/* hero */
.hero{position:absolute;left:0;top:125px;width:1200px;height:585px}
.hero-photo{position:absolute;inset:0;background:linear-gradient(180deg,#3f8fd8 0%,#6fb2e8 45%,#a9c8dc 68%,#6c7f91 82%,#2b5f8a 100%)}
.hero-caption{position:absolute;left:200px;top:407px;width:800px;height:108px;background:rgba(40,40,40,.55);display:flex;align-items:center;justify-content:center}
.hero-caption h1{font-family:'Oswald',sans-serif;font-weight:400;font-size:52px;line-height:1;color:var(--white);letter-spacing:.3px;white-space:nowrap}
.hero-dots{position:absolute;top:533px;left:538px;display:flex;gap:20px}
.hero-dots span{width:28px;height:6px;background:var(--lime)}
.hero-dots .is-current{background:var(--white)}
.hero-rule{position:absolute;left:0;top:710px;width:1200px;height:5px;background:var(--lime)}

/* who */
.who{position:absolute;left:0;top:715px;width:1200px;height:342px;background:var(--teal);color:var(--white);text-align:center}
.section-title{font-size:26px;font-weight:400;text-transform:uppercase}
.who .section-title{margin-top:32px}
.who p{width:1000px;margin:22px auto 0;font-size:11.5px;line-height:20px}
.btn-dark{display:inline-block;background:var(--dark);color:var(--white);font-size:12px;font-weight:500;padding:12px 20px;border-radius:2px;text-transform:uppercase}
.who .btn-dark{margin-top:24px}
.wedge{position:absolute;left:0;width:1200px}

/* why */
.why-photo{left:100px;top:1107px;width:472px;height:275px;background:linear-gradient(135deg,#d9d4cb,#a7a29a 50%,#8a6c58);border:1px solid #ddd}
.why{left:600px;top:1075px;width:505px}
.why .section-title{color:#222;font-size:25px}
.why ul{list-style:none;margin-top:20px}
.why li{position:relative;padding-left:27px;font-size:12px;line-height:18px;margin-bottom:11px;color:#333}
.why li svg{position:absolute;left:0;top:2px}

/* mission */
.mission-band{position:absolute;left:0;top:1420px;width:1200px;height:362px;background:linear-gradient(100deg,#7fbf3a,#9bd04e 60%,#8cc63f)}
.statement{position:absolute;top:1510px;width:470px;color:var(--white)}
.statement h2{font-size:26px;font-weight:400;text-transform:uppercase}
.statement h3{font-size:16px;font-weight:500;margin-top:8px;line-height:22px}
.statement p{font-size:11px;line-height:19px;margin-top:10px;opacity:.92}
.statement .btn-dark{position:absolute;top:195px;left:0}

/* reviews */
.reviews-title{left:0;top:1818px;width:1200px;text-align:center;color:#222;font-size:25px}
.review{position:absolute;top:1882px;width:322px}
.review-photo{height:188px;border:1px solid #ddd}
.review-meta{display:flex;align-items:center;gap:12px;margin-top:14px;font-size:12px;color:var(--red)}
.review h4{font-size:16px;font-weight:500;color:#222;margin-top:10px}
.review p{font-size:12.5px;line-height:18px;color:var(--muted);margin-top:6px}
.carousel-arrow{position:absolute;top:1945px}

/* footer */
.site-footer{position:absolute;left:0;top:2214px;width:1200px;height:279px;background:var(--footer);color:var(--white)}
.footer-col{position:absolute;top:46px}
.footer-col h5{font-size:20px;font-weight:400;margin-bottom:22px}
.footer-col li{list-style:none;font-size:12px;font-weight:500;line-height:25px}
.footer-divider{position:absolute;top:40px;width:1px;height:140px;background:rgba(255,255,255,.35)}
.newsletter p{font-size:11.5px;line-height:24px}
.news-form{display:flex;margin-top:14px}
.news-input{width:205px;height:38px;border:1px solid rgba(255,255,255,.7);font-size:11px;padding:12px 10px;color:var(--white)}
.news-go{width:45px;height:38px;background:var(--dark);font-size:14px;display:flex;align-items:center;justify-content:center}
.social li{display:flex;align-items:center;gap:16px}
.social .dot{width:8px;height:8px;border-radius:50%;background:var(--white)}
.copyright{position:absolute;top:242px;width:1200px;text-align:center;font-size:11px}
</style>
</head>
<body>

<header class="site-header">
  <div class="brand"><span class="brand-mark"></span><span class="brand-name">Craft Beacon K.V.</span></div>
  <div class="account"><a class="btn-signup" href="#">Sign-up</a><a href="#">Register</a></div>
  <nav class="main-nav">
    <a class="is-active" href="#">Home</a><a href="#">About</a><a href="#">Who we are</a><a href="#">Partners</a><a href="#">Links</a><a href="#">Training</a><a href="#">Contact</a>
  </nav>
</header>

<section class="hero">
  <div class="hero-photo" role="img" aria-label="Toronto skyline across the lake with the RB Spire under a blue sky"></div>
  <div class="hero-caption"><h1>THE CRAFT BEACON K.V PROGRAM</h1></div>
  <div class="hero-dots"><span></span><span class="is-current"></span><span></span></div>
</section>
<div class="hero-rule"></div>

<section class="who">
  <h2 class="section-title">Who we are...</h2>
  <p>The Craft Beacon K.V Program is a twelve week skill and employment-based training program that links young men and women from under-resourced communities to apprenticeship career opportunities in the construction industry that they might otherwise have difficulty accessing. Participants are exposed to multiple construction trades over the course of the program. There is hands-on learning at various affiliate training centres located across the GTA in addition to jobsite visits. Participants are provided with leadership and mentoring from seasoned construction workers with years of work experience and learn valuable skill sets which build self-confidence and promote positive self-awareness.</p>
  <a class="btn-dark" href="#">Self-assessment quiz</a>
</section>
<svg class="wedge" style="top:985px" width="1200" height="73" viewBox="0 0 1200 73"><polygon points="0,73 600,4 1200,73" fill="#fff"/></svg>

<div class="abs why-photo" role="img" aria-label="Instructor and students working together around a table"></div>
<section class="abs why">
  <h2 class="section-title">Why choose us?</h2>
  <ul>
    <li><svg width="14" height="14" viewBox="0 0 14 14"><circle cx="7" cy="7" r="7" fill="#f0642a"/><path d="M5.5 4 L8.5 7 L5.5 10" stroke="#fff" stroke-width="1.8" fill="none"/></svg>Shorter programs with over 70% hands-on training gets students workforce ready earlier than most other programs.</li>
    <li><svg width="14" height="14" viewBox="0 0 14 14"><circle cx="7" cy="7" r="7" fill="#f0642a"/><path d="M5.5 4 L8.5 7 L5.5 10" stroke="#fff" stroke-width="1.8" fill="none"/></svg>Over 17,000 square feet of fully-equipped shop space provides students with a full-scale experience.</li>
    <li><svg width="14" height="14" viewBox="0 0 14 14"><circle cx="7" cy="7" r="7" fill="#f0642a"/><path d="M5.5 4 L8.5 7 L5.5 10" stroke="#fff" stroke-width="1.8" fill="none"/></svg>Students are trained by experienced instructors who work in the field and know the industry.</li>
    <li><svg width="14" height="14" viewBox="0 0 14 14"><circle cx="7" cy="7" r="7" fill="#f0642a"/><path d="M5.5 4 L8.5 7 L5.5 10" stroke="#fff" stroke-width="1.8" fill="none"/></svg>Tuition includes tools, textbooks, on-site parking, personal protective equipment and safety certifications – No hidden fees!</li>
    <li><svg width="14" height="14" viewBox="0 0 14 14"><circle cx="7" cy="7" r="7" fill="#f0642a"/><path d="M5.5 4 L8.5 7 L5.5 10" stroke="#fff" stroke-width="1.8" fill="none"/></svg>Develop essential technical abilities, critical employability skills and gain experience to excel as skilled workers.</li>
    <li><svg width="14" height="14" viewBox="0 0 14 14"><circle cx="7" cy="7" r="7" fill="#f0642a"/><path d="M5.5 4 L8.5 7 L5.5 10" stroke="#fff" stroke-width="1.8" fill="none"/></svg>Successful graduates receive personalized job search assistance to help them land their first job in the trade!</li>
  </ul>
</section>

<div class="mission-band" role="img" aria-label="Faint construction crane scene in green tones"></div>
<svg class="wedge" style="top:1419px" width="1200" height="50" viewBox="0 0 1200 50"><polygon points="0,0 1200,0 1200,8 600,45 0,8" fill="#fff"/></svg>

<section class="statement" style="left:100px">
  <h2>Our mission</h2>
  <h3>Provide people with opportunities to build a better future</h3>
  <p>The Institute for Skills Growth &amp; Learning (The Institute) along with Maple Ridge High School (MRHS) provides adult and continuing education services. The Institute evolved from the adult education department of the Lakeview District School Board to become a financially independent, not-for-profit organization, delivering free government-funded programs to help people at all stages of life (youth, job seekers and newcomers to Canada)</p>
  <a class="btn-dark" href="#">Read more</a>
</section>
<section class="statement" style="left:628px">
  <h2>Our vision</h2>
  <h3>be the recognized leader in career and workforce development, in support of strong communities.</h3>
  <p>MRHS offers adult, alternative and continuing education credit-based programs, working with The Institute to collectively serve over 25,000 people annually through multiple sites in Lakeview Region and Westbrook. Together, MRHS and The Institute extend the reach of the LDSB to support people of all ages, bridging the gap for learners between high school.</p>
  <a class="btn-dark" href="#">Read more</a>
</section>

<h2 class="abs section-title reviews-title">Our training reviews</h2>
<svg class="carousel-arrow" style="left:72px" width="16" height="70" viewBox="0 0 16 70"><path d="M15 1 L2 35 L15 69" stroke="#bbb" stroke-width="1.5" fill="none"/></svg>
<svg class="carousel-arrow" style="left:1112px" width="16" height="70" viewBox="0 0 16 70"><path d="M1 1 L14 35 L1 69" stroke="#bbb" stroke-width="1.5" fill="none"/></svg>

<article class="review" style="left:99px">
  <div class="review-photo" role="img" aria-label="Hands reviewing building plans beside a hard hat" style="background:linear-gradient(135deg,#e9ecef,#b9c4cc 55%,#5a6470)"></div>
  <div class="review-meta"><span>february 11, 2016</span><svg width="86" height="14" viewBox="0 0 86 14"><g fill="#f5b400"><polygon points="7,0 9,5 14,5 10,8 11.5,13 7,10 2.5,13 4,8 0,5 5,5"/><polygon transform="translate(18 0)" points="7,0 9,5 14,5 10,8 11.5,13 7,10 2.5,13 4,8 0,5 5,5"/><polygon transform="translate(36 0)" points="7,0 9,5 14,5 10,8 11.5,13 7,10 2.5,13 4,8 0,5 5,5"/><polygon transform="translate(54 0)" points="7,0 9,5 14,5 10,8 11.5,13 7,10 2.5,13 4,8 0,5 5,5"/><polygon transform="translate(72 0)" points="7,0 7,10 2.5,13 4,8 0,5 5,5"/></g></svg></div>
  <h4>Personal protective equipment</h4>
  <p>Accusantium doloremque laudantium, totam rem eriam, eaque ipsa quae ab illo inventore veritatis.</p>
</article>
<article class="review" style="left:439px">
  <div class="review-photo" role="img" aria-label="Student studying at a desk with a laptop" style="background:linear-gradient(135deg,#f3ede2,#e1c9a8 55%,#c86a4a)"></div>
  <div class="review-meta"><span>february 11, 2016</span><svg width="86" height="14" viewBox="0 0 86 14"><g fill="#f5b400"><polygon points="7,0 9,5 14,5 10,8 11.5,13 7,10 2.5,13 4,8 0,5 5,5"/><polygon transform="translate(18 0)" points="7,0 9,5 14,5 10,8 11.5,13 7,10 2.5,13 4,8 0,5 5,5"/><polygon transform="translate(36 0)" points="7,0 9,5 14,5 10,8 11.5,13 7,10 2.5,13 4,8 0,5 5,5"/><polygon transform="translate(54 0)" points="7,0 9,5 14,5 10,8 11.5,13 7,10 2.5,13 4,8 0,5 5,5"/><polygon transform="translate(72 0)" points="7,0 7,10 2.5,13 4,8 0,5 5,5"/></g></svg></div>
  <h4>Students are trained by</h4>
  <p>Accusantium doloremque laudantium, totam rem eriam, eaque ipsa quae ab illo inventore veritatis.</p>
</article>
<article class="review" style="left:779px">
  <div class="review-photo" role="img" aria-label="Construction workers in hard hats building a brick wall" style="background:linear-gradient(135deg,#d7e2ea,#b08a68 55%,#6b4a34)"></div>
  <div class="review-meta"><span>february 11, 2016</span><svg width="86" height="14" viewBox="0 0 86 14"><g fill="#f5b400"><polygon points="7,0 9,5 14,5 10,8 11.5,13 7,10 2.5,13 4,8 0,5 5,5"/><polygon transform="translate(18 0)" points="7,0 9,5 14,5 10,8 11.5,13 7,10 2.5,13 4,8 0,5 5,5"/><polygon transform="translate(36 0)" points="7,0 9,5 14,5 10,8 11.5,13 7,10 2.5,13 4,8 0,5 5,5"/><polygon transform="translate(54 0)" points="7,0 9,5 14,5 10,8 11.5,13 7,10 2.5,13 4,8 0,5 5,5"/><polygon transform="translate(72 0)" points="7,0 7,10 2.5,13 4,8 0,5 5,5"/></g></svg></div>
  <h4>Develop essential technical</h4>
  <p>Accusantium doloremque laudantium, totam rem eriam, eaque ipsa quae ab illo inventore veritatis.</p>
</article>

<footer class="site-footer">
  <div class="footer-col" style="left:100px"><h5>Our Link</h5>
    <ul><li>Home</li><li>About</li><li>Who We Are</li><li>Partners</li><li>Links...</li></ul></div>
  <div class="footer-divider" style="left:237px"></div>
  <div class="footer-col" style="left:293px"><h5>Contact US</h5>
    <ul><li>Serving All South Florida</li><li>hello@craftbeacon.com</li><li>+1 555-010-4821</li></ul></div>
  <div class="footer-divider" style="left:515px"></div>
  <div class="footer-col newsletter" style="left:595px"><h5>Newsletter</h5>
    <p>Dolore magnam aliquam quaerat voluptatem.<br>Ut enim blanditiis praesentium voluptatum</p>
    <div class="news-form"><span class="news-input">Enter Your Email</span><span class="news-go">GO!</span></div></div>
  <div class="footer-divider" style="left:930px"></div>
  <div class="footer-col social" style="left:1003px"><h5>Follow Us</h5>
    <ul><li><span class="dot"></span>friendsnet</li><li><span class="dot"></span>chirpline</li><li><span class="dot"></span>snapgram</li><li><span class="dot"></span>circlesphere</li></ul></div>
  <p class="copyright">@ Copy Rights -2016 CraftBeacon.com - All rights reserved.</p>
</footer>

</body>
</html>
```